Management Consultancy needs sharp professional services showcased in a brochure

We are a management consultancy specializing on contract management and conflict avoidance services requiring a professional brochure showcasing our services to prospective clients.

Attached are a selection of existing stationary and the colour scheme.

Further details on our company can be found at www.velto-advisory-partners.com
Updates

Preference is for bi-fold, however, innovative tri-fold will be considered. Added Monday, August 7, 2017

Target Market(s)

Construction companies, consultants, developers, oil and gas service providers, NGO's, SME's.

Industry/Entity Type

Management

Requirements
Must have
• High degree of professionalism with eye catching, sharp detail. No frils.
• Colour scheme as per the attachments
• Font as per attachments - Century Gothic
• Details of our company and services
Nice to have
• Open to ideas, thinking along the lines of a car brochure type design.
• Bi-fold preferred, by trifold accepted if innovative.
Should not have
• Remove reference to the United Arab Emirates.
• No cartoon/clipart photos.

```html
<!DOCTYPE html>
<html lang="en">
<head>
<meta charset="utf-8">
<title>Velto Advisory – Bi-fold Brochure</title>
<link rel="stylesheet" href="https://fonts.googleapis.com/css2?family=Didact+Gothic&family=Montserrat:wght@600;700&display=swap">
<style>
  :root {
    --backdrop: #2a2a2c;
    --navy: #2d3b58;
    --navy-soft: #3a4866;
    --slate: #4a5874;
    --red: #a3232c;
    --white: #ffffff;
    --ink-light: #d9deea;
    --paper: #f4f5f8;
  }
  * { box-sizing: border-box; margin: 0; padding: 0; }
  html, body { width: 1200px; height: 789px; overflow: hidden; background: var(--backdrop); }
  body { position: relative; font-family: "Didact Gothic", sans-serif; }

  .spread { position: absolute; left: 180px; top: 97px; width: 840px; height: 594px; display: flex; box-shadow: 0 18px 40px rgba(0,0,0,.55); }
  .page { position: relative; width: 420px; height: 594px; overflow: hidden; }

  /* Back page */
  .page--about { background: var(--navy); color: var(--ink-light); padding: 44px 40px 0 44px; }
  .page--about .swirl { position: absolute; inset: 0; pointer-events: none; }
  .about__title { font-family: "Montserrat", sans-serif; font-weight: 700; font-size: 17px; color: var(--white); letter-spacing: .5px; position: relative; }
  .about__title span { font-family: "Didact Gothic", sans-serif; font-weight: 400; }
  .about__rule { height: 1px; background: rgba(255,255,255,.5); width: 100%; margin: 6px 0 10px; position: relative; }
  .about__body { position: relative; font-size: 7.2px; line-height: 1.45; }
  .about__body p { margin-bottom: 7px; }
  .about__body .lead { font-size: 8.6px; }
  .sectors { list-style: none; margin: 2px 0 8px; }
  .sectors li { font-family: "Montserrat", sans-serif; font-weight: 600; color: var(--white); font-size: 7.4px; line-height: 1.55; padding-left: 14px; position: relative; }
  .sectors li::before { content: ""; position: absolute; left: 0; top: 3px; width: 7px; height: 5px; border: 1px solid var(--white); border-top: none; border-radius: 0 0 4px 4px; }
  .about__quote { font-family: "Montserrat", sans-serif; font-weight: 700; color: var(--white); font-size: 7.8px; line-height: 1.45; }
  .brand { display: flex; align-items: center; gap: 8px; font-family: "Didact Gothic", sans-serif; letter-spacing: 1px; }
  .brand__dot { width: 12px; height: 12px; border-radius: 50%; }
  .page--about .brand { position: absolute; right: 40px; top: 450px; color: var(--white); font-size: 19px; }
  .page--about .brand__dot { background: var(--white); }
  .contact { position: absolute; left: 44px; bottom: 30px; font-size: 8.6px; color: var(--white); list-style: none; }
  .contact li { display: flex; align-items: center; gap: 7px; margin-top: 4px; }
  .contact svg { width: 9px; height: 9px; }
  .page--about .edge { position: absolute; left: 0; bottom: 0; width: 100%; height: 5px; background: var(--red); }

  /* Cover */
  .page--cover { background: var(--paper); }
  .cover__photo { position: absolute; left: 0; top: 0; width: 420px; height: 380px; background: linear-gradient(120deg, #e8ebf0 0%, #b9c1cf 35%, #5e6d88 62%, #2c3a57 100%); }
  .cover__title-block { position: absolute; left: 0; top: 405px; width: 170px; height: 189px; background: var(--slate); }
  .cover__red-block { position: absolute; left: 150px; top: 380px; width: 110px; height: 214px; background: var(--red); }
  .cover__title { position: absolute; left: 22px; top: 468px; color: var(--white); font-family: "Montserrat", sans-serif; font-weight: 700; font-size: 18px; line-height: 1.05; }
  .cover__title .and { display: block; font-family: "Didact Gothic", sans-serif; font-weight: 400; font-size: 15px; }
  .cover__title .small { font-size: 14px; }
  .cover__panel { position: absolute; left: 240px; top: 330px; width: 180px; height: 150px; background: var(--white); display: flex; align-items: center; justify-content: center; border-left: 4px solid var(--navy); }
  .cover__panel .brand { color: var(--navy); font-size: 17px; }
  .cover__panel .brand__dot { background: var(--red); }
  .cover__strip { position: absolute; left: 240px; top: 480px; width: 180px; height: 40px; background: var(--red); color: var(--white); font-size: 8.4px; display: flex; align-items: center; justify-content: center; gap: 6px; }
  .cover__strip svg { width: 9px; height: 9px; }
</style>
</head>
<body>
  <main class="spread">
    <section class="page page--about">
      <svg class="swirl" viewBox="0 0 420 594" aria-hidden="true">
        <path d="M-40 420 Q200 300 460 380" fill="none" stroke="rgba(255,255,255,.05)" stroke-width="40"/>
        <path d="M-40 520 Q220 420 460 500" fill="none" stroke="rgba(255,255,255,.04)" stroke-width="30"/>
      </svg>
      <h1 class="about__title">ABOUT <span>US</span></h1>
      <div class="about__rule"></div>
      <div class="about__body">
        <p class="lead">We are an experienced contract and conflict advisory providing global contract performance solutions and conflict management to:</p>
        <ul class="sectors">
          <li>International Development Organisations;</li>
          <li>Construction Industry;</li>
          <li>Oil And Gas Industry; And</li>
          <li>Government Sectors.</li>
        </ul>
        <p>Observing the standard of consultancy services and magnitude of contractual engagements and conflicts, we see the opportunity to make things better: better engagements, better awareness, better performance, which all lead to better value in terms of financial benefit and relationship maintenance. We firmly believe in party success in a non litigious environment.</p>
        <p>Our services are uniquely delivered through our integrated management consultancy model, with a single point of contact and responsibility, and focused attention to detail. We provide advisory services and solutions resolving past and current claims, and in doing so, preparing our clients for a conflict free future based on our core principles of integrity, equality and strength, ensuring compliance and experience at an intimate professional level. We aim to have our clients feel our principles in our presence and in our advisories, giving the service which is deserved.</p>
        <p class="lead">Our clients range from Global 500 companies, international contractors to government bodies and authorities.</p>
        <p>Velto Advisory is more than just a professional advisory consultancy; we are an integrated professional team with deep domain expertise, industry knowledge and the ability to work across multiple jurisdictions supported by a wide professional network.</p>
        <p>We forge strong client partnerships and in doing so, we develop and maintain these relationships through performance and delivery of professional services which create and maximise value for our clients.</p>
        <p>Through our unique approach to contract and conflict management, we want the best for our clients to ensure that contract integrity, compliance and performance is maintained with the upmost faith, based around our principles.</p>
        <p class="about__quote">"If value, whether financial or relationship is not achieved, then we are not finished, we have only just begun."</p>
      </div>
      <div class="brand"><span class="brand__dot"></span>Velto Advisory</div>
      <ul class="contact">
        <li><svg viewBox="0 0 10 10"><rect x="0.5" y="2" width="9" height="6" fill="none" stroke="#fff"/><path d="M0.5 2 L5 5.5 L9.5 2" fill="none" stroke="#fff"/></svg>jmorrow@velto-advisory-partners.com</li>
        <li><svg viewBox="0 0 10 10"><circle cx="5" cy="5" r="4.3" fill="none" stroke="#fff"/><path d="M0.7 5 H9.3 M5 0.7 Q2 5 5 9.3 Q8 5 5 0.7" fill="none" stroke="#fff" stroke-width=".8"/></svg>www.velto-advisory-partners.com</li>
      </ul>
      <div class="edge"></div>
    </section>

    <section class="page page--cover">
      <div class="cover__photo" role="img" aria-label="Photo of two consultants in suits reviewing a document on a tablet in a bright office"></div>
      <div class="cover__title-block"></div>
      <div class="cover__red-block"></div>
      <h2 class="cover__title">THE<br>CONTRACT<span class="and">AND</span><span class="small">CONFLICT ADVISORY</span></h2>
      <div class="cover__panel"><div class="brand"><span class="brand__dot"></span>Velto Advisory</div></div>
      <div class="cover__strip"><svg viewBox="0 0 10 10"><circle cx="5" cy="5" r="4.3" fill="none" stroke="#fff"/><path d="M0.7 5 H9.3 M5 0.7 Q2 5 5 9.3 Q8 5 5 0.7" fill="none" stroke="#fff" stroke-width=".8"/></svg>www.velto-advisory-partners.com</div>
    </section>
  </main>
</body>
</html>
```